International Employee Benefits

Create website including logo for Dunmore Global
Specialising in setting up and managing employee benefits for multi-national companies
Should be professional and simple to navigate
Updates

Company name is Dunmore Global

Please ensure the following is adhered to :

Page size - 950 pixels wide

If you plan to use a texture or picture background please ensure these are tiled so that the left edge matches the right edge like wallpaper.

The home page should have the logo at the top left of the screen followed by tabs "About Us", "Resources" "Expertise" "References" "Contact Us"
Perhaps there can also be an image on the home page, something that signifies global success??

The wording on the home page should be:

 Dunmore Global brings a results oriented approach partnering with clients in mapping out customized strategies that meet their international objectives that save time and money and leaves an established process in place.  The client is supported with a high touch, one point of contact, that bring solutions to complex problems

 

Target Market(s)

Companies - HR and Finance

Industry/Entity Type

Employee

Requirements
Must have
• Map of world or globe

```html
<!DOCTYPE html>
<html lang="en">
<head>
<meta charset="utf-8">
<title>Dunmore Global – International Employee Benefits</title>
<link rel="stylesheet" href="https://fonts.googleapis.com/css2?family=Arimo:wght@400;700&family=Ubuntu:wght@400;500&display=swap">
<style>
:root{
  --blue:#1a74c0;
  --blue-dark:#1556a8;
  --nav-top:#4d8ee0;
  --nav-bottom:#1b58b8;
  --ink:#111;
  --muted:#666;
  --band:#ececec;
  --footer:#333;
  --rule:#dcdcdc;
}
*{box-sizing:border-box;margin:0;padding:0}
html,body{width:1102px;height:1200px;overflow:hidden;background:#fff;font-family:"Arimo",Arial,sans-serif}
.page{position:relative;width:1102px;height:1200px;border-top:5px solid #9b9b9b}
.brand{position:absolute;left:96px;top:22px;display:flex;align-items:center;gap:18px}
.brand-dot{width:66px;height:66px;border-radius:50%;background:var(--blue)}
.brand-name{font-family:"Ubuntu",sans-serif;font-weight:500;font-size:29px;line-height:31px;color:var(--blue)}
.util{position:absolute;right:96px;top:24px;font-family:"Ubuntu",sans-serif;font-size:12.5px;color:#555}
.lang{position:absolute;right:101px;top:65px;display:flex;align-items:center;gap:8px;font-family:"Ubuntu",sans-serif;font-size:12.5px;color:#222}
.lang-select{width:94px;height:24px;border:1px solid #ccc;border-radius:3px;display:flex;align-items:center;gap:8px;padding:0 7px;font-size:11.5px;color:#333;background:linear-gradient(#fff,#f1f1f1)}
.lang-select .flag{width:18px;height:12px;background:#27408b}
.nav{position:absolute;left:96px;top:120px;width:910px;height:42px;border-radius:21px;background:linear-gradient(var(--nav-top),var(--nav-bottom));display:flex;align-items:center;padding-left:38px}
.nav a{color:#fff;text-decoration:none;font-size:15px;padding:0 16px;line-height:42px}
.nav a.active{background:#000;padding:0 11px;margin-right:6px}
.hero{position:absolute;left:0;top:190px;width:1102px;height:456px;border-top:5px solid #e6e6e6;background:linear-gradient(100deg,#c9d7e0 0%,#dfe6ea 35%,#6e8fb8 60%,#a9bccc 80%,#c4d0d8 100%)}
.hero-panel{position:absolute;left:97px;top:115px;width:438px;height:283px;background:rgba(255,255,255,.82);padding:16px 29px 0 17px}
.hero-panel h1{font-family:"Ubuntu",sans-serif;font-weight:400;font-size:34px;line-height:43px;color:var(--blue);margin-bottom:10px}
.hero-panel p{font-family:"Ubuntu",sans-serif;font-size:12.5px;line-height:19.2px;color:var(--ink);text-align:justify}
.btn-blue{display:inline-block;margin-top:13px;width:98px;height:29px;border-radius:4px;background:linear-gradient(#3a86d8,var(--blue-dark));color:#fff;font-family:"Ubuntu",sans-serif;font-size:13.5px;line-height:29px;text-align:center}
.hero-next{position:absolute;left:967px;top:213px;width:38px;height:38px;border-radius:50%;background:rgba(255,255,255,.5)}
.hero-bottom{position:absolute;left:0;top:646px;width:1102px;height:5px;background:#e6e6e6}
.cols{position:absolute;top:680px;left:105px;display:flex;gap:21px}
.col{width:282px}
.col h2{font-weight:400;font-size:17px;color:var(--blue);padding-left:5px;margin-bottom:9px}
.thumb{height:135px;border:1px solid var(--rule);padding:5px}
.thumb div{width:100%;height:100%}
.col p{margin-top:11px;font-size:12.5px;line-height:21px;color:var(--muted);text-align:justify;height:126px}
.btn-grey{display:inline-block;width:79px;height:27px;border-radius:3px;background:linear-gradient(#7c7c7c,#555);color:#fff;font-size:12.5px;line-height:27px;text-align:center;box-shadow:0 2px 2px rgba(0,0,0,.25)}
.login{position:absolute;left:0;top:1056px;width:1102px;height:56px;background:var(--band)}
.login svg{position:absolute;left:196px;top:8px}
.login-title{position:absolute;left:240px;top:16px;font-size:19px;color:var(--blue)}
.field{position:absolute;top:12px;width:204px;height:31px;background:#fff;border:1px solid #ccc;font-size:12px;color:#999;padding:9px 14px}
.submit{position:absolute;left:821px;top:14px;width:79px;height:27px;border-radius:3px;background:linear-gradient(#777,#4a4a4a);color:#fff;font-size:14px;line-height:27px;text-align:center}
.footer{position:absolute;left:0;top:1119px;width:1102px;height:81px;background:var(--footer);color:#fff;font-size:12px}
.footer-links{position:absolute;left:96px;top:18px}
.footer-links span{margin:0 7px}
.copy{position:absolute;left:96px;top:50px;word-spacing:2px}
.social{position:absolute;left:954px;top:28px;display:flex;gap:5px}
.social i{width:23px;height:23px;border-radius:4px;display:block}
</style>
</head>
<body>
<div class="page">
  <header>
    <div class="brand"><span class="brand-dot"></span><span class="brand-name">Dunmore<br>Global</span></div>
    <div class="util">Contact Us | Sitemap</div>
    <div class="lang">Select Language : <span class="lang-select"><span class="flag"></span>English ⌄</span></div>
    <nav class="nav">
      <a class="active" href="#">HOME</a><a href="#">AT A GLANCE</a><a href="#">CLIENT ADVOCATE</a><a href="#">OTHER RESOURCES</a><a href="#">CONTACT US</a>
    </nav>
  </header>

  <section class="hero" role="img" aria-label="Photo of a large globe rising behind a city skyline reflected on water, a man on a pier looking on">
    <div class="hero-panel">
      <h1>INTERNATIONAL<br>EMPLOYEE BENEFITS</h1>
      <p>Dunmore Global is ready to Bridge The Gap between our client’s international needs and objectives. Through education, strengthened communications and laying a foundation with processes, Dunmore Global will ensure that future international needs and objectives will continue to be met. Our model is based on client advocacy, teamwork and partnership. Let us know your thoughts.</p>
      <span class="btn-blue">READ MORE</span>
    </div>
    <svg class="hero-next" viewBox="0 0 38 38"><path d="M16 12l7 7-7 7" fill="none" stroke="#fff" stroke-width="2"/></svg>
  </section>
  <div class="hero-bottom"></div>

  <section class="cols">
    <article class="col">
      <h2>AT A GLANCE</h2>
      <div class="thumb"><div role="img" aria-label="Photo of business people reviewing documents at a desk" style="background:linear-gradient(90deg,#8aa6c4,#3b4d6b 55%,#c9d6e4)"></div></div>
      <p>Dunmore Global specializes in the design and funding of employee benefit plans for local national employees in over 90 countries. We assist in the establishment of new benefit plans and analyze current plans, bench marking against local best practices.</p>
      <span class="btn-grey">View more</span>
    </article>
    <article class="col">
      <h2>CLIENT ADVOCATE</h2>
      <div class="thumb"><div role="img" aria-label="Photo of two business people shaking hands" style="background:linear-gradient(90deg,#1e2230,#9fb0c2 45%,#d6a48a 55%,#5a6272)"></div></div>
      <p>Cultural awareness is a major key to meeting client objectives and taking client advocacy beyond normal expectations. Our goal is to create a global strategy whereby all parties have aligned expectations and future results can be measured against original goals</p>
      <span class="btn-grey">View more</span>
    </article>
    <article class="col">
      <h2>OTHER RESOURCES</h2>
      <div class="thumb"><div role="img" aria-label="Illustration of a computer monitor showing charts beside a falling line graph" style="background:linear-gradient(90deg,#e9e9e9,#cfd3d8 40%,#f0f0f0)"></div></div>
      <p>International employee benefit plans require more than advice and recommendations. They require ancillary support and Dunmore Global has established legal, accounting and payroll resources for our client’s referral.</p>
      <span class="btn-grey">View more</span>
    </article>
  </section>

  <section class="login">
    <svg width="32" height="40" viewBox="0 0 32 40"><circle cx="20" cy="10" r="8" fill="#777"/><circle cx="20" cy="8" r="2.5" fill="#ececec"/><path d="M16 16L6 34l3 3 3-4-2-2 3-2-1-2 6-11z" fill="#888"/></svg>
    <span class="login-title">Member Login</span>
    <span class="field" style="left:394px">User name</span>
    <span class="field" style="left:606px">Pass word</span>
    <span class="submit">SUBMIT</span>
  </section>

  <footer class="footer">
    <div class="footer-links">Home<span>|</span>About Us<span>|</span>Resource<span>|</span>Expertise<span>|</span>References<span>|</span>Contact Us</div>
    <div class="copy">Copyright © 2013 www.dunmoreglobal.com &nbsp; All rights reserved.</div>
    <div class="social"><i style="background:#3b5a9a"></i><i style="background:#3fa9e0"></i></div>
  </footer>
</div>
</body>
</html>
```